Business Card Design Project

I am a Chiropractor that is looking for a new business card.  Our logo was slightly changed lately, therefore need a new, more professional look.
We are a modern, non-stuffy chiropractic office.  Want a contemporary look that will let people know this is not your typical doctors office.  Our logo is red, and contains the name of our business: realign.  The u in the logo is green, stressing the most important part of our business: "u"

Target Market(s)
moderate to upper income bracket, family friendly
www.realignspine-example.com
Gordon Pell
Family Chiropractor
314 Hollis Rd
Bastrop, TX 78999
512.555.0147 phone
512.555.0148 fax
Industry/Entity Type
Business
Requirements
Must have
- www.realignspine-example.com
Gordon Pell
Family Chiropractor
314 Hollis Rd
Bastrop, TX 78999
512.555.0147 phone
512.555.0148 fax

```html
<!DOCTYPE html>
<html lang="en">
<head>
<meta charset="utf-8">
<title>realign – business card</title>
<link rel="stylesheet" href="https://fonts.googleapis.com/css2?family=Open+Sans:wght@300;400;600&display=swap">
<style>
  :root {
    --page-bg: #e9e7e5;
    --brand-red: #e8322a;
    --brand-red-dark: #c9211b;
    --brand-red-light: #f0675c;
    --brand-green: #5ab031;
    --ink-grey: #4a4a4a;
    --card-white: #ffffff;
    --hairline: #f3a29c;
  }
  * { margin: 0; padding: 0; box-sizing: border-box; }
  html, body {
    width: 1200px; height: 955px; overflow: hidden;
    background: var(--page-bg);
    font-family: "Open Sans", Arial, sans-serif;
  }
  .stage {
    position: relative; width: 1200px; height: 955px;
  }
  .card {
    position: absolute; left: 250px; width: 700px; height: 400px;
    border-radius: 26px; overflow: hidden;
    box-shadow: 0 6px 18px rgba(0,0,0,0.18);
  }
  /* front */
  .card-front { top: 40px; background: var(--card-white); }
  .front-band {
    position: absolute; left: 0; top: 0; width: 700px; height: 92px;
  }
  .badge-circle {
    position: absolute; left: 34px; top: 14px; width: 66px; height: 66px;
    border-radius: 50%; background: var(--card-white);
    border: 3px solid var(--brand-red-dark);
  }
  .front-wordmark {
    position: absolute; right: 34px; top: 6px;
    font-weight: 300; font-size: 66px; line-height: 80px;
    color: var(--card-white); letter-spacing: 1px;
  }
  .practice-info {
    position: absolute; left: 40px; top: 128px;
    color: var(--brand-red); font-size: 19px; line-height: 23px;
  }
  .contact-list {
    position: absolute; left: 40px; top: 196px; list-style: none;
    color: var(--ink-grey); font-size: 19px; line-height: 27px;
  }
  .contact-list li { display: flex; align-items: center; gap: 12px; }
  .contact-icon { width: 16px; height: 16px; flex: none; }
  .person {
    position: absolute; right: 48px; bottom: 46px; text-align: right;
  }
  .person-name { color: var(--brand-red); font-size: 31px; line-height: 38px; }
  .person-title { color: var(--brand-green); font-size: 17px; line-height: 20px; }
  /* back */
  .card-back {
    top: 500px;
    background: linear-gradient(160deg, var(--brand-red-light) 0%, var(--brand-red) 55%, var(--brand-red-dark) 100%);
  }
  .back-wordmark {
    position: absolute; left: 40px; top: 40px;
    font-weight: 300; font-size: 190px; line-height: 220px;
    color: rgba(255,255,255,0.28); letter-spacing: 2px;
  }
  .back-web {
    position: absolute; left: 40px; bottom: 34px;
    color: rgba(255,255,255,0.85); font-size: 17px;
  }
</style>
</head>
<body>
<main class="stage">

  <section class="card card-front">
    <svg class="front-band" viewBox="0 0 700 92" aria-hidden="true">
      <defs>
        <linearGradient id="bandFill" x1="0" y1="0" x2="0" y2="1">
          <stop offset="0" stop-color="#f0473d"/>
          <stop offset="1" stop-color="#d9261f"/>
        </linearGradient>
      </defs>
      <path d="M0 0 H700 V78 Q420 70 120 84 Q60 86 0 90 Z" fill="url(#bandFill)"/>
      <path d="M0 92 Q60 88 120 86 Q420 72 700 80" fill="none" stroke="var(--hairline)" stroke-width="2"/>
    </svg>
    <div class="badge-circle"></div>
    <div class="front-wordmark">realign</div>

    <div class="practice-info">
      <p>Family Chiropractor</p>
      <p>314 Hollis Rd Bastrop, TX 78999</p>
    </div>

    <ul class="contact-list">
      <li>
        <svg class="contact-icon" viewBox="0 0 16 16" aria-hidden="true"><path d="M3 1 L6 1 L7 5 L5 6.5 Q6.5 9.5 9.5 11 L11 9 L15 10 L15 13 Q15 15 13 15 Q1 14 1 3 Q1 1 3 1 Z" fill="var(--brand-red)"/></svg>
        512.555.0147
      </li>
      <li>
        <svg class="contact-icon" viewBox="0 0 16 16" aria-hidden="true"><rect x="1" y="1" width="14" height="14" rx="3" fill="var(--brand-red)"/><rect x="4" y="4" width="8" height="3" fill="#fff"/><rect x="4" y="9" width="8" height="3" fill="#fff"/></svg>
        512.555.0148
      </li>
      <li>
        <svg class="contact-icon" viewBox="0 0 16 16" aria-hidden="true"><rect x="1" y="3" width="14" height="10" rx="1.5" fill="var(--brand-red)"/><path d="M1.5 4 L8 9 L14.5 4" fill="none" stroke="#fff" stroke-width="1.4"/></svg>
        info@realignspine-example.com
      </li>
      <li>
        <svg class="contact-icon" viewBox="0 0 16 16" aria-hidden="true"><circle cx="8" cy="8" r="7" fill="var(--brand-red)"/><path d="M1 8 H15 M8 1 Q4 8 8 15 M8 1 Q12 8 8 15" fill="none" stroke="#fff" stroke-width="1.1"/></svg>
        www.realignspine-example.com
      </li>
    </ul>

    <div class="person">
      <p class="person-name">Gordon Pell</p>
      <p class="person-title">General Manager</p>
    </div>
  </section>

  <section class="card card-back">
    <div class="back-wordmark">realign</div>
    <p class="back-web">www.realignspine-example.com</p>
  </section>

</main>
</body>
</html>
```